Calloway Dental Care

I need a nice business card design that is double sided. This is for a dental surgery. I have already had a logo designed and just need the business card put together.

It needs to be in a format such that I can make new business cards if new dentists begin working for me. Hence I need to be able to change the text in order to have new names written on new cards.

The front will have the following text:

Dr Tariq Mansour
B. Med. Sci. QBTU B.Dent. Brel. Uni

The logo will appear somewhere on the front. This is attached.

In addition will be the following writing that also needs to appear on the front of the card, perhaps at the bottom on the left side will be:

Shop 4, 212-240 Parlow Street, Harwick Vale, ELR, 2999

and at the bottom on the right side will be:
(02) 5550 1736
e: info@callowaydentalcare.com.au
www.callowaydentalcare.com.au

On the back of the card will be a section for a map to be drawn (I have uploaded a picture) and also a section written as follows:

"Your next appointment is: (a line needs to be here to write date and time)"

Also I need two lines for two appointments to be written.

Thanks for your efforts!

```html
<!DOCTYPE html>
<html lang="en">
<head>
<meta charset="utf-8">
<title>Calloway Dental Care – Business Card</title>
<link rel="stylesheet" href="https://fonts.googleapis.com/css2?family=Oswald:wght@500&family=Abel&family=Arimo:wght@700&display=swap">
<style>
  :root {
    --page: #e9e7e4;
    --back-card: #b9b9b9;
    --front-dark: #121c1c;
    --front-dark-2: #1d2b2b;
    --accent: #f5a623;
    --brand-blue: #3d79c2;
    --brand-cyan: #3fd4dd;
    --ink: #1c1c1c;
    --white: #ffffff;
    --map-warm: #f2c46a;
    --map-road: #e27a52;
    --map-grey: #a9a9a9;
  }
  * { box-sizing: border-box; margin: 0; padding: 0; }
  html, body { width: 1200px; height: 1000px; overflow: hidden; }
  body { background: var(--page); position: relative; font-family: "Abel", sans-serif; }

  .card {
    position: absolute;
    top: 577px;
    width: 588px;
    height: 362px;
    overflow: hidden;
  }
  .card--back { left: 12px; background: var(--back-card); }
  .card--front {
    left: 600px;
    background: linear-gradient(160deg, var(--front-dark-2) 0%, var(--front-dark) 60%);
  }

  /* brand name block (shared) */
  .brand {
    position: absolute;
    width: 160px;
    text-align: center;
    font-family: "Abel", sans-serif;
    color: var(--brand-blue);
    font-size: 22px;
    line-height: 1.05;
    letter-spacing: 1px;
    text-transform: uppercase;
  }
  .brand__dot {
    display: block;
    width: 60px; height: 60px;
    margin: 0 auto 14px;
    border-radius: 50%;
    background: var(--brand-cyan);
  }
  .card--back .brand { left: 393px; top: 28px; }
  .card--front .brand { left: 397px; top: 28px; }

  /* back side */
  .map {
    position: absolute;
    left: 52px; top: 58px;
    width: 310px; height: 196px;
    border-radius: 4px;
    background: linear-gradient(135deg, var(--map-road) 0%, var(--map-grey) 35%, var(--map-warm) 75%, var(--map-grey) 100%);
    opacity: 0.85;
  }
  .appointment {
    position: absolute;
    left: 40px; top: 292px;
    font-family: "Arimo", sans-serif;
    font-weight: 700;
    font-size: 14px;
    color: var(--ink);
  }
  .appointment__line {
    position: absolute;
    left: 222px;
    width: 196px;
    border-top: 1.5px dashed var(--ink);
  }
  .appointment__line--one { top: 306px; }
  .appointment__line--two { top: 325px; }

  /* front side */
  .accent-rule {
    position: absolute;
    left: 36px;
    width: 3px;
    background: var(--accent);
  }
  .accent-rule--top { top: 0; height: 113px; }
  .accent-rule--bottom { top: 268px; height: 94px; }

  .dentist {
    position: absolute;
    left: 41px; top: 184px;
    color: var(--white);
  }
  .dentist__name {
    font-family: "Oswald", sans-serif;
    font-weight: 500;
    font-size: 24px;
    letter-spacing: 0.5px;
    line-height: 1.1;
    text-transform: uppercase;
  }
  .dentist__surname { color: var(--accent); }
  .dentist__credentials { font-size: 10.5px; margin-top: 2px; }

  .detail {
    display: flex;
    align-items: center;
    gap: 8px;
    font-size: 11px;
    color: var(--white);
  }
  .detail__icon {
    display: inline-flex;
    align-items: center;
    justify-content: center;
    width: 12px; height: 10px;
    background: var(--white);
    color: var(--front-dark);
    font-size: 7px;
    border-radius: 1px;
  }
  .address { position: absolute; left: 41px; top: 237px; }

  .divider {
    position: absolute;
    left: 341px; top: 200px;
    width: 2px; height: 96px;
    background: var(--white);
  }
  .contacts {
    position: absolute;
    left: 400px; top: 236px;
    display: flex;
    flex-direction: column;
    gap: 5px;
  }
</style>
</head>
<body>

<section class="card card--back" aria-label="Card back">
  <div class="map" role="img" aria-label="Street map showing the location of Calloway Dental Care"></div>
  <div class="brand"><span class="brand__dot"></span>Calloway<br>Dental Care</div>
  <p class="appointment">Your Next Appointment :</p>
  <span class="appointment__line appointment__line--one"></span>
  <span class="appointment__line appointment__line--two"></span>
</section>

<section class="card card--front" aria-label="Card front">
  <span class="accent-rule accent-rule--top"></span>
  <span class="accent-rule accent-rule--bottom"></span>
  <div class="brand"><span class="brand__dot"></span>Calloway<br>Dental Care</div>

  <div class="dentist">
    <h1 class="dentist__name">Dr Tariq <span class="dentist__surname">Mansour</span></h1>
    <p class="dentist__credentials">B. Med. Sci. QBTU B.Dent. Brel. Uni</p>
  </div>

  <p class="detail address"><span class="detail__icon">A</span>Shop 4, 212-240 Parlow Street, Harwick Vale, ELR, 2999</p>

  <span class="divider"></span>

  <div class="contacts">
    <p class="detail"><span class="detail__icon">T</span>(02) 5550 1736</p>
    <p class="detail"><span class="detail__icon">E</span>info@callowaydentalcare.com.au</p>
    <p class="detail"><span class="detail__icon">W</span>www.callowaydentalcare.com.au</p>
  </div>
</section>

</body>
</html>
```